Gutschein-Design für Friseursalon gesucht
Zielgruppe
Wir sind ein Friseursalon für Jung bis Alt.
Wir bieten alles rund um das Haar an und verkaufen Haarpflegeprodukte.
Aufgabenstellung
Das Design sollte Modern und Professionell wirken.
Ebenso muss es zu unserem Firmenlogo passen.
Es sollte auf die Rückseite des Gutscheins ein Feld für den Betrag, für Wen, das Datum, den Stempel und die Gutscheinnummer vorhanden sein.

```html
<!DOCTYPE html>
<html lang="de">
<head>
<meta charset="utf-8">
<title>Gutschein – Lockenstudio Veri</title>
<link href="https://fonts.googleapis.com/css2?family=Arimo:ital,wght@0,400;0,700;1,700&display=swap" rel="stylesheet">
<style>
  :root {
    --purple: #8e2a8b;
    --paper: #ffffff;
    --voucher-tint: #f3e4f1;
    --ink: #2b2b2b;
    --ink-soft: #555555;
    --field: #ffffff;
  }
  * { box-sizing: border-box; margin: 0; padding: 0; }
  html, body { width: 1200px; height: 1200px; overflow: hidden; background: var(--paper); }
  body { position: relative; font-family: "Arimo", Arial, sans-serif; color: var(--ink); }

  /* Front side */
  .card-front {
    position: absolute; left: 217px; top: 204px; width: 718px; height: 341px;
    overflow: hidden; background: #eeecee;
  }
  .front-photo {
    position: absolute; left: 71px; top: 0; width: 647px; height: 341px;
    background:
      radial-gradient(ellipse 38% 70% at 62% 48%, rgba(160,155,162,.45) 0%, rgba(200,196,201,.25) 55%, rgba(230,228,231,0) 100%),
      linear-gradient(90deg, #efedef 0%, #e8e5e9 40%, #dcd8dd 70%, #e4dae4 100%);
  }
  .front-band {
    position: absolute; left: 0; top: 0; width: 71px; height: 100%;
    background: var(--purple);
  }
  .front-band span {
    position: absolute; left: 50%; top: 50%;
    transform: translate(-50%, -50%) rotate(-90deg);
    color: #fff; font-size: 50px; letter-spacing: 1px; white-space: nowrap;
  }
  .brand-name {
    position: absolute; font-family: "Arimo", Arial, sans-serif; font-weight: 400;
    color: var(--ink); white-space: nowrap; display: flex; align-items: center; gap: 7px;
  }
  .brand-name i { display: inline-block; border-radius: 50%; background: var(--ink); }
  .card-front .brand-name { left: 100px; top: 38px; font-size: 22px; }
  .card-front .brand-name i { width: 10px; height: 10px; }

  .info-disc {
    position: absolute; left: 89px; top: 118px; width: 200px; height: 200px; border-radius: 50%;
    background: linear-gradient(135deg, #f1f0f1 0%, #d6d4d7 55%, #c2bfc3 100%);
  }
  .info-text { position: absolute; left: 121px; top: 150px; }
  .owner-name { color: var(--purple); font-size: 14px; }
  .owner-role { font-size: 9.5px; color: var(--ink-soft); margin-top: 2px; }
  .address { font-size: 14px; line-height: 17px; margin-top: 18px; }
  .phone { display: flex; align-items: center; gap: 8px; margin-top: 18px; margin-left: 16px; }
  .phone svg { width: 20px; height: 36px; }
  .phone b { font-size: 17px; font-style: italic; font-weight: 700; }

  /* Back side */
  .card-back {
    position: absolute; left: 217px; top: 624px; width: 718px; height: 338px;
    background: var(--voucher-tint);
  }
  .back-title {
    position: absolute; left: 27px; top: 28px; font-size: 47px; color: var(--purple); font-weight: 400;
  }
  .number-label { position: absolute; left: 460px; top: 59px; font-size: 9.5px; color: var(--ink-soft); }
  .field { position: absolute; background: var(--field); font-size: 11px; color: var(--ink-soft); padding: 7px 6px; }
  .field-number { left: 553px; top: 32px; width: 125px; height: 38px; }
  .field-amount { left: 27px; top: 96px; width: 651px; height: 29px; }
  .field-words  { left: 27px; top: 130px; width: 651px; height: 28px; }
  .field-for    { left: 27px; top: 164px; width: 651px; height: 29px; }
  .field-date   { left: 27px; top: 200px; width: 297px; height: 101px; }
  .fine-print { position: absolute; left: 34px; top: 313px; font-size: 8px; color: var(--ink-soft); }
  .card-back .brand-name { left: 492px; top: 228px; font-size: 20px; }
  .card-back .brand-name i { width: 9px; height: 9px; }
</style>
</head>
<body>

<section class="card-front">
  <div class="front-photo" role="img" aria-label="Schwarzweiß-Porträtfoto eines Models mit hellem Haar und violettem Make-up"></div>
  <div class="front-band"><span>GUTSCHEIN</span></div>
  <div class="brand-name"><i></i>Lockenstudio Veri</div>
  <div class="info-disc"></div>
  <div class="info-text">
    <p class="owner-name">Veri Sonnfeld</p>
    <p class="owner-role">Inhaberin Friseurmeisterin</p>
    <p class="address">Mühlengasse 7<br>54329 Kornbach</p>
    <div class="phone">
      <svg viewBox="0 0 20 36" aria-hidden="true">
        <path d="M6 2 C2 4 1 10 1 18 C1 26 2 32 6 34 L9 32 L7 24 L5 24 C4 20 4 16 5 12 L7 12 L9 4 Z" fill="#2b2b2b"/>
      </svg>
      <b>06512 - 4870</b>
    </div>
  </div>
</section>

<section class="card-back">
  <h2 class="back-title">GUTSCHEIN</h2>
  <span class="number-label">Gutscheinnummer:</span>
  <div class="field field-number"></div>
  <div class="field field-amount">Über</div>
  <div class="field field-words">in Worten</div>
  <div class="field field-for">Für</div>
  <div class="field field-date">Datum</div>
  <p class="fine-print">Dieser Gutschein kann nicht gegen Bargeld eingelöst werden</p>
  <div class="brand-name"><i></i>Lockenstudio Veri</div>
</section>

</body>
</html>
```